Brennick Holdings Business Cards

These are professional business cards that are for my family office.
Put fake emails and phone numbers as of now until I finalize those components. This family office controls my families investments, assets, and future. The cards should be professional.
..
.
.
.
I just uploaded another variation of a logo I would like to see as a business card to I am inbeteen which logo to use

Target Market(s)

business

Industry/Entity Type

business

Contact Information for Business Card

Professional, wealth related, finance related.

Requirements
Must have
• Logo

```html
<!DOCTYPE html>
<html lang="en">
<head>
<meta charset="utf-8">
<title>Brennick Holdings Business Cards</title>
<link rel="stylesheet" href="https://fonts.googleapis.com/css2?family=Montserrat:wght@500;600&family=Arimo:wght@400&display=swap">
<style>
  :root {
    --page: #efefef;
    --card: #1b1b1b;
    --accent: #d58a2c;
    --ink-light: #ffffff;
    --ink-dark: #1b1b1b;
    --ring-faint: #2b2b2b;
  }
  html, body {
    margin: 0;
    padding: 0;
    width: 1200px;
    height: 1000px;
    overflow: hidden;
    background: var(--page);
  }
  .canvas {
    position: relative;
    width: 1200px;
    height: 1000px;
  }
  .card {
    position: absolute;
    left: 287px;
    width: 796px;
    height: 455px;
    background: var(--card);
    border-radius: 22px;
    overflow: hidden;
  }
  .card--front { top: 32px; }
  .card--back { top: 512px; }

  /* Front */
  .brand-ring {
    position: absolute;
    left: 272px;
    top: 45px;
    width: 256px;
    height: 256px;
  }
  .front-name {
    position: absolute;
    left: 0;
    right: 0;
    top: 334px;
    text-align: center;
    font-family: "Montserrat", sans-serif;
    font-weight: 500;
    font-size: 24px;
    line-height: 28px;
    letter-spacing: 1.5px;
    text-transform: uppercase;
    color: var(--ink-light);
  }
  .front-web {
    position: absolute;
    left: 0;
    right: 0;
    top: 402px;
    display: flex;
    justify-content: center;
    align-items: center;
    gap: 14px;
    font-family: "Arimo", sans-serif;
    font-size: 18px;
    letter-spacing: 4px;
    color: var(--ink-light);
  }
  .front-web .dot {
    width: 9px;
    height: 9px;
    border-radius: 50%;
    background: var(--accent);
  }

  /* Back */
  .back-ring {
    position: absolute;
    left: 490px;
    top: 72px;
    width: 256px;
    height: 256px;
  }
  .person {
    position: absolute;
    left: 39px;
    top: 126px;
  }
  .person-name {
    margin: 0;
    font-family: "Montserrat", sans-serif;
    font-weight: 500;
    font-size: 30px;
    letter-spacing: 3px;
    text-transform: uppercase;
    color: var(--accent);
    line-height: 34px;
  }
  .person-title {
    margin: 8px 0 0;
    font-family: "Montserrat", sans-serif;
    font-weight: 600;
    font-size: 20px;
    line-height: 24px;
    letter-spacing: 0.5px;
    text-transform: uppercase;
    color: var(--ink-light);
  }
  .contacts {
    position: absolute;
    left: 40px;
    top: 218px;
    margin: 0;
    padding: 0;
    list-style: none;
    font-family: "Arimo", sans-serif;
    font-size: 20px;
    color: var(--ink-light);
  }
  .contacts li {
    display: flex;
    align-items: flex-start;
    gap: 11px;
    margin-bottom: 7px;
    line-height: 26px;
  }
  .contacts li:last-child { margin-top: 2px; line-height: 31px; }
  .contact-icon {
    flex: none;
    width: 21px;
    height: 21px;
    margin-top: 3px;
  }
  .back-name {
    position: absolute;
    right: 50px;
    top: 384px;
    font-family: "Montserrat", sans-serif;
    font-weight: 500;
    font-size: 22px;
    line-height: 28px;
    letter-spacing: 1.5px;
    text-transform: uppercase;
    color: var(--ink-light);
  }
</style>
</head>
<body>
<main class="canvas">

  <section class="card card--front" aria-label="Card front">
    <svg class="brand-ring" viewBox="0 0 256 256" aria-hidden="true">
      <circle cx="128" cy="128" r="123" fill="none" stroke="var(--ink-light)" stroke-width="5"/>
    </svg>
    <div class="front-name">Brennick Holdings</div>
    <div class="front-web"><span class="dot"></span>WWW.BRENNICKHOLD.COM<span class="dot"></span></div>
  </section>

  <section class="card card--back" aria-label="Card back">
    <svg class="back-ring" viewBox="0 0 256 256" aria-hidden="true">
      <circle cx="128" cy="128" r="123" fill="none" stroke="var(--ring-faint)" stroke-width="4"/>
    </svg>

    <div class="person">
      <h1 class="person-name">Adrian Kessler</h1>
      <p class="person-title">Managing Director</p>
    </div>

    <ul class="contacts">
      <li>
        <svg class="contact-icon" viewBox="0 0 21 21" aria-hidden="true">
          <rect width="21" height="21" rx="3" fill="var(--accent)"/>
          <rect x="4" y="4" width="5" height="13" rx="1" fill="var(--ink-dark)"/>
          <rect x="10" y="5" width="7" height="12" rx="1" fill="var(--ink-dark)"/>
          <rect x="11.5" y="6.5" width="4" height="2.5" fill="var(--accent)"/>
          <rect x="11.5" y="10.5" width="1.5" height="1.5" fill="var(--accent)"/>
          <rect x="14" y="10.5" width="1.5" height="1.5" fill="var(--accent)"/>
          <rect x="11.5" y="13.5" width="1.5" height="1.5" fill="var(--accent)"/>
          <rect x="14" y="13.5" width="1.5" height="1.5" fill="var(--accent)"/>
        </svg>
        <span>044-987 654 321</span>
      </li>
      <li>
        <svg class="contact-icon" viewBox="0 0 21 21" aria-hidden="true">
          <rect width="21" height="21" rx="3" fill="var(--accent)"/>
          <path d="M17 4 L3 10 L8 12 L15 6 L9.5 13 L9.5 17 L12 14 L15 16 Z" fill="var(--ink-dark)"/>
        </svg>
        <span>hello@brennickmail.com</span>
      </li>
      <li>
        <svg class="contact-icon" viewBox="0 0 21 21" aria-hidden="true">
          <rect width="21" height="21" rx="3" fill="var(--accent)"/>
          <path d="M10.5 3.5 C7.4 3.5 5.5 5.7 5.5 8.3 C5.5 11.6 10.5 17.5 10.5 17.5 C10.5 17.5 15.5 11.6 15.5 8.3 C15.5 5.7 13.6 3.5 10.5 3.5 Z" fill="var(--ink-light)"/>
          <circle cx="10.5" cy="8.4" r="2" fill="var(--accent)"/>
        </svg>
        <span>4417 Harbor Crest Blvd,<br>210-B, FL 32541</span>
      </li>
    </ul>

    <div class="back-name">Brennick Holdings</div>
  </section>

</main>
</body>
</html>
```